Travel Group 'Halvard Group' needs a new business card design

Halvard Group is a diverse business specialising in bespoke, tailor made holidays to suit all budgets and we are specialists in planning exciting day/short trips to suit all markets. Our target market is very varied going from the corporate client and as well as people in the community who simply want to experience something special.
We are looking for a card design that will encourage people to look at our websites and social media platforms and to see for themselves the different facets to our business. It is essential that the card has social media icons for Pagebloom, Quibbly and Snapverse. We are looking for a card with a blank background with no pictures and for the front side to have the attached Halvard logo. The card should have similar colour scheme to the attached Halvard logo.
The card must have the following information on one side:
Maren Doyle
Business Development Manager
marendoyle@halvardtravel.example
Halvard Group, 48 Fenwick Row
Marrowfield, Dunmoreshire, Northmere KB27 4RT
+44 (0)1632 960418
And then the card must have the following on the second side:
(Halvard logo)
(social media icons)
www.halvardtravel.example
www.halvardexperience.example
Target Market(s)
Our target market is very varied going from the corporate client and as well as people in the community who simply want to experience something special.
Industry/Entity Type
Business
Contact Information for Business Card
Maren Doyle
+44 (0)1632 960418
(Halvard logo)
(social media icons)
www.halvardtravel.example
www.halvardexperience.example
Requirements
Must have
- It is essential that the card has social media icons for Pagebloom, Quibbly & Snapverse.
Should not have
- Should not have any images other than Halvard logo.

```html
<!DOCTYPE html>
<html lang="en">
<head>
<meta charset="utf-8">
<title>Halvard Group – Business Card</title>
<link rel="stylesheet" href="https://fonts.googleapis.com/css2?family=Hind:wght@400;500;600&display=swap">
<style>
  :root {
    --page-bg: #e4e4e4;
    --card-bg: #ffffff;
    --ink: #3b3e55;
    --ink-dark: #2a2c3c;
    --indigo: #2a2359;
    --plum: #6a1f6e;
    --magenta: #d8088a;
    --dot-pagebloom: #1b8ad8;
    --dot-quibbly: #ee5c8a;
    --dot-snapverse: #4bb8e8;
    --icon-grey: #7a7c88;
  }
  * { box-sizing: border-box; margin: 0; padding: 0; }
  html, body { width: 1200px; height: 1000px; overflow: hidden; }
  body {
    background: var(--page-bg);
    font-family: "Hind", sans-serif;
    color: var(--ink);
    position: relative;
  }
  .card {
    position: absolute;
    width: 672px;
    height: 384px;
    background: var(--card-bg);
    overflow: hidden;
  }
  .card-back { left: 458px; top: 77px; }
  .card-front { left: 142px; top: 506px; width: 675px; height: 387px; }
  .card svg.card-art { position: absolute; inset: 0; width: 100%; height: 100%; }
  .abs { position: absolute; white-space: nowrap; }

  /* Back side */
  .brand-name {
    left: 0; width: 100%; top: 136px; padding-left: 356px;
    text-align: left;
    font-weight: 600; font-size: 34px; letter-spacing: 3px;
    color: #ffffff; line-height: 1;
  }
  .brand-name span { display: inline-block; transform: translateX(-50%); }
  .social-item { top: 297px; display: flex; align-items: center; gap: 12px; font-size: 17px; color: var(--ink-dark); }
  .social-dot { width: 30px; height: 30px; border-radius: 50%; display: inline-block; }
  .social-pagebloom { left: 34px; }
  .social-pagebloom .social-dot { background: var(--dot-pagebloom); }
  .social-quibbly { left: 265px; }
  .social-quibbly .social-dot { background: var(--dot-quibbly); }
  .social-snapverse { left: 495px; }
  .social-snapverse .social-dot { background: var(--dot-snapverse); }
  .web-links { top: 338px; left: 0; width: 100%; text-align: center; font-size: 16px; color: var(--ink-dark); }

  /* Front side */
  .person-name { left: 113px; top: 70px; font-size: 32px; color: var(--ink); line-height: 1.2; }
  .person-title { left: 36px; top: 106px; font-size: 21px; color: var(--ink); line-height: 1.2; }
  .contact-row { left: 300px; display: flex; align-items: center; gap: 16px; font-size: 19px; color: var(--ink); }
  .contact-row svg { width: 22px; height: 22px; }
  .contact-phone { top: 196px; }
  .contact-email { top: 230px; }
  .address { left: 0; width: 100%; top: 317px; text-align: center; font-size: 16px; line-height: 20px; color: var(--ink); }
</style>
</head>
<body>

<section class="card card-back" aria-label="Card back">
  <svg class="card-art" viewBox="0 0 672 384" aria-hidden="true">
    <defs>
      <linearGradient id="bandGradient" x1="0" y1="0" x2="1" y2="0">
        <stop offset="0" stop-color="var(--indigo)"/>
        <stop offset="0.5" stop-color="var(--plum)"/>
        <stop offset="1" stop-color="var(--magenta)"/>
      </linearGradient>
    </defs>
    <rect width="672" height="384" fill="url(#bandGradient)"/>
    <path d="M0,247 C110,300 240,292 380,238 C480,198 560,160 672,212 L672,384 L0,384 Z" fill="#ffffff"/>
    <path d="M0,228 C100,276 240,274 360,226 C470,182 560,132 672,190" fill="none" stroke="#ffffff" stroke-width="2"/>
  </svg>
  <div class="abs brand-name"><span>HALVARD</span></div>
  <div class="abs social-item social-pagebloom"><span class="social-dot"></span>Pagebloom</div>
  <div class="abs social-item social-quibbly"><span class="social-dot"></span>Quibbly</div>
  <div class="abs social-item social-snapverse"><span class="social-dot"></span>Snapverse</div>
  <div class="abs web-links">www.halvardtravel.example / www.halvardexperience.example</div>
</section>

<section class="card card-front" aria-label="Card front">
  <svg class="card-art" viewBox="0 0 675 387" aria-hidden="true">
    <defs>
      <linearGradient id="lineGradient" x1="0" y1="0" x2="1" y2="0">
        <stop offset="0" stop-color="var(--indigo)"/>
        <stop offset="0.55" stop-color="var(--plum)"/>
        <stop offset="1" stop-color="var(--magenta)"/>
      </linearGradient>
    </defs>
    <path d="M0,175 C55,202 105,213 160,212 C300,210 420,102 546,102 C600,102 640,118 675,140" fill="none" stroke="url(#lineGradient)" stroke-width="2.5"/>
  </svg>
  <div class="abs person-name">Maren Doyle</div>
  <div class="abs person-title">Business Development Manager</div>
  <div class="abs contact-row contact-phone">
    <svg viewBox="0 0 24 24" aria-hidden="true"><path fill="var(--icon-grey)" d="M6.6 10.8c1.4 2.8 3.8 5.1 6.6 6.6l2.2-2.2c.3-.3.7-.4 1-.2 1.1.4 2.3.6 3.6.6.6 0 1 .4 1 1V20c0 .6-.4 1-1 1C10.6 21 3 13.4 3 4c0-.6.4-1 1-1h3.5c.6 0 1 .4 1 1 0 1.3.2 2.5.6 3.6.1.3 0 .7-.2 1z"/></svg>
    <span>+44 (0)1632 960418</span>
  </div>
  <div class="abs contact-row contact-email">
    <svg viewBox="0 0 24 24" aria-hidden="true"><rect x="2" y="5" width="20" height="14" fill="var(--icon-grey)"/><path d="M2.5 5.5 L12 13 L21.5 5.5" fill="none" stroke="#ffffff" stroke-width="1.5"/></svg>
    <span>marendoyle@halvardtravel.example</span>
  </div>
  <div class="abs address">Halvard Group, 48 Fenwick Row<br>Marrowfield, Dunmoreshire, Northmere KB27 4RT</div>
</section>

</body>
</html>
```